Business Card Design - Furniture Retail

Open to both Single or double sided design

We are launching a online ecommerce store that sells Scandinavian/Danish style of furniture in Australia.

We aspire to provide stylish but classic and designers' selection of furniture to the Australia public at affordable price. For the style of the furniture we are selling, please see the following links:

https://www.boxlyshare.com/sh/qrk7vz2mwpl04tn/BBXTpeLr3h52Kd7nWqYzRsGmu?dl=0

The style of the design we are looking for is clean, simple that look Scandinavian/Danish but yet it is timeless classic.

Aspiring Design
http://www.hallwick.com
http://brenlowe.com.au/
http://kolvo.furniture/
http://www.tipo.com/
Updates

Please display the card on normal angle for both front and back instead of funny angle. Please keep it display when displaying the design of the business cards so that we can focus on the designs rather than being confused by the unnecessary stuffs like the hands or background

I think there is already enough curve line on the logo itself so anything extra of the curve on the business card would be really unnecessary. Please avoid using any of the extra curve line on the business card, other than the logo itself. Thanks

Regular card and give them a matt celloglaze to create texture on card that makes it looked luxury and expensive.

Please display design on normal angle! Please only use white colour in the background (not the business card but the referring to the submission) rather than anything fancy so that we can focus on the design.

Target Market(s)

High end market consumers who are financially capable and who has good taste and appreciate good design

aged between 28 - 45 white collars professional/businessmen who live in metropolitan areas

Industry/Entity Type

Business

Font styles to use
Serif
Sans Serif

Requirements
Must have
• Regular card and give them a matt celloglaze to create texture on card that makes it looked luxury and expensive.

Please use the logo from the uploaded files

Company Name: Miles Orveda
Name: Peter Holm
Phone: +614 27 505 316
Website: www.milesorveda.com.au
Email: peter@milesorveda.com.au
Nice to have
• Colour is not limited to black and white
Should not have
• The concept photos of the furniture should NOT be used in the FRONT page of the business card.

```html
<!DOCTYPE html>
<html lang="en">
<head>
<meta charset="utf-8">
<title>Miles Orveda — Business Card</title>
<link rel="stylesheet" href="https://fonts.googleapis.com/css2?family=Lato:wght@400;700&display=swap">
<style>
  :root {
    --page: #ffffff;
    --frost-light: #f3f2f1;
    --frost-mid: #e4e2e0;
    --frost-warm: #eadcdc;
    --ink: #2e2c2c;
    --panel: #0c0c0c;
    --panel-edge: #1c1b1a;
    --gold: #c9a982;
    --gold-light: #e6d3bb;
    --silver: #d8d6d4;
  }
  html, body {
    margin: 0;
    padding: 0;
    width: 1200px;
    height: 970px;
    overflow: hidden;
    background: var(--page);
    font-family: "Lato", "Helvetica Neue", Arial, sans-serif;
  }
  .canvas {
    position: relative;
    width: 1200px;
    height: 970px;
  }
  .card {
    position: absolute;
    left: 150px;
    top: 232px;
    width: 900px;
    height: 505px;
    overflow: hidden;
    box-shadow: 0 10px 30px rgba(0,0,0,0.18);
    border: 1px solid #d0cfcd;
  }
  .card__front {
    position: absolute;
    left: 0; top: 0;
    width: 430px; height: 100%;
    background: linear-gradient(180deg, var(--frost-light) 0%, var(--frost-mid) 55%, var(--frost-warm) 80%, var(--frost-mid) 100%);
  }
  .brand-name {
    position: absolute;
    left: 0; width: 430px;
    top: 238px;
    margin: 0;
    text-align: center;
    font-weight: 400;
    font-size: 36px;
    letter-spacing: 2px;
    color: var(--ink);
  }
  .card__back {
    position: absolute;
    left: 430px; top: 0;
    width: 470px; height: 100%;
    background: radial-gradient(ellipse at 70% 20%, var(--panel-edge) 0%, var(--panel) 60%);
  }
  .divider {
    position: absolute;
    left: 0; top: 0;
    width: 60px; height: 505px;
  }
  .holder-name {
    position: absolute;
    right: 44px;
    top: 76px;
    margin: 0;
    font-size: 27px;
    font-weight: 700;
    letter-spacing: 1px;
    color: var(--gold-light);
  }
  .contact {
    position: absolute;
    right: 42px;
    top: 312px;
    margin: 0;
    padding: 0;
    list-style: none;
  }
  .contact__item {
    display: flex;
    justify-content: flex-end;
    align-items: center;
    height: 31px;
    font-size: 18px;
    letter-spacing: 0.5px;
    color: var(--gold);
  }
  .contact__item--person { color: var(--silver); }
  .contact__icon {
    width: 18px; height: 18px;
    margin-left: 12px;
    fill: var(--silver);
  }
</style>
</head>
<body>
<main class="canvas">
  <section class="card">
    <div class="card__front">
      <p class="brand-name">MILES ORVEDA</p>
    </div>
    <div class="card__back">
      <svg class="divider" viewBox="0 0 60 505" aria-hidden="true">
        <rect x="0" y="0" width="10" height="505" fill="#1a1918"/>
        <polyline points="17,0 17,60 40,80 17,100 17,300 40,320 17,340 17,505"
                  fill="none" stroke="#c9a982" stroke-width="3"/>
      </svg>
      <h1 class="holder-name">MILES ORVEDA</h1>
      <ul class="contact">
        <li class="contact__item contact__item--person">PETER HOLM
          <svg class="contact__icon" viewBox="0 0 18 18" aria-hidden="true"><circle cx="9" cy="5" r="4"/><path d="M1 18c0-5 3.5-8 8-8s8 3 8 8z"/></svg>
        </li>
        <li class="contact__item">+614 27 505 316
          <svg class="contact__icon" viewBox="0 0 18 18" aria-hidden="true"><path d="M1 6c0-3 4-4 8-4s8 1 8 4v2h-4V6H5v2H1z"/><path d="M4 9h10l2 7H2z"/></svg>
        </li>
        <li class="contact__item">PETER@MILESORVEDA.COM.AU
          <svg class="contact__icon" viewBox="0 0 18 18" aria-hidden="true"><path d="M1 4h16v11H1z M2.5 5.5 9 10.5l6.5-5" fill="none" stroke="#d8d6d4" stroke-width="1.6"/></svg>
        </li>
        <li class="contact__item">WWW.MILESORVEDA.COM.AU
          <svg class="contact__icon" viewBox="0 0 18 18" aria-hidden="true"><path d="M1 3h16v10H1z M3 5v6h12V5z"/><rect x="7" y="13" width="4" height="2"/><rect x="5" y="15" width="8" height="1.6"/></svg>
        </li>
      </ul>
    </div>
  </section>
</main>
</body>
</html>
```